First Aid Training business needs business card design

We would like a double sided business card designed for a first aid training business - Brindlewood First Aid. We provide first aid training and , WHS (work, health and safety) training.

The attached word document contains the key information we would like on each side of the business card.

Final design needs to be delivered in print ready format, along with the original file.

```html
<!DOCTYPE html>
<html lang="en">
<head>
<meta charset="utf-8">
<title>Brindlewood First Aid — Business Card</title>
<link rel="stylesheet" href="https://fonts.googleapis.com/css2?family=Lato:wght@400&family=Montserrat:wght@700&display=swap">
<style>
  :root {
    --backdrop: #aeafae;
    --card-white: #ffffff;
    --accent-red: #e3262b;
    --ink-black: #111111;
    --text-grey: #4d4d4d;
    --title-grey: #6a6a6a;
    --back-grey-light: #8c8c8c;
    --back-grey-dark: #767676;
    --back-ink: #3f3f3f;
    --back-mark: #ececec;
  }
  html, body {
    margin: 0;
    padding: 0;
    width: 1200px;
    height: 1200px;
    overflow: hidden;
    background: var(--backdrop);
  }
  .canvas {
    position: relative;
    width: 1200px;
    height: 1200px;
  }
  .card {
    position: absolute;
    left: 222px;
    width: 756px;
    height: 463px;
    border-radius: 36px;
    overflow: hidden;
  }
  .card--front {
    top: 109px;
    background: var(--card-white);
  }
  .card--back {
    top: 630px;
    background: linear-gradient(160deg, var(--back-grey-light), var(--back-grey-dark));
  }

  /* Front: brand block */
  .brand {
    position: absolute;
    left: 70px;
    top: 110px;
    width: 260px;
    text-align: center;
  }
  .brand__dot {
    display: block;
    width: 92px;
    height: 92px;
    margin: 0 auto 22px;
    border-radius: 50%;
    background: var(--accent-red);
  }
  .brand__name {
    margin: 0;
    font-family: "Montserrat", sans-serif;
    font-weight: 700;
    font-size: 29px;
    line-height: 1.15;
    color: var(--ink-black);
    text-transform: uppercase;
  }
  .divider {
    position: absolute;
    left: 363px;
    top: 121px;
    width: 3px;
    height: 222px;
    background: var(--ink-black);
  }

  /* Front: person + contacts */
  .person {
    position: absolute;
    left: 406px;
    top: 117px;
    font-family: "Lato", sans-serif;
  }
  .person__name {
    margin: 0;
    font-size: 39px;
    line-height: 1;
    font-weight: 400;
    color: var(--accent-red);
  }
  .person__title {
    margin: 8px 0 0;
    font-size: 22px;
    color: var(--title-grey);
  }
  .contacts {
    list-style: none;
    margin: 0;
    padding: 0;
    position: absolute;
    left: 406px;
    top: 224px;
    font-family: "Lato", sans-serif;
    font-size: 21px;
    color: var(--text-grey);
  }
  .contacts__item {
    display: flex;
    align-items: center;
    height: 31px;
  }
  .contacts__icon {
    width: 20px;
    height: 20px;
    margin-right: 10px;
    fill: var(--accent-red);
    flex: none;
  }

  /* Back */
  .back-brand {
    position: absolute;
    left: 0;
    right: 0;
    top: 80px;
    text-align: center;
  }
  .back-brand__dot {
    display: block;
    width: 130px;
    height: 130px;
    margin: 0 auto 34px;
    border-radius: 50%;
    background: var(--back-mark);
  }
  .back-brand__name {
    margin: 0 auto;
    width: 340px;
    font-family: "Montserrat", sans-serif;
    font-weight: 700;
    font-size: 38px;
    line-height: 1.15;
    color: var(--back-ink);
    text-transform: uppercase;
  }
</style>
</head>
<body>
<main class="canvas">

  <section class="card card--front" aria-label="Business card front">
    <div class="brand">
      <span class="brand__dot"></span>
      <p class="brand__name">Brindlewood First Aid</p>
    </div>

    <div class="divider"></div>

    <div class="person">
      <h1 class="person__name">Marcus Whitfield</h1>
      <p class="person__title">Account Executive</p>
    </div>

    <ul class="contacts">
      <li class="contacts__item">
        <svg class="contacts__icon" viewBox="0 0 24 24" aria-hidden="true"><path d="M6.6 10.8a15 15 0 0 0 6.6 6.6l2.2-2.2a1 1 0 0 1 1-.25 11.4 11.4 0 0 0 3.6.57 1 1 0 0 1 1 1V20a1 1 0 0 1-1 1A17 17 0 0 1 3 4a1 1 0 0 1 1-1h3.5a1 1 0 0 1 1 1c0 1.25.2 2.45.57 3.6a1 1 0 0 1-.25 1z"/></svg>
        415.555.0142
      </li>
      <li class="contacts__item">
        <svg class="contacts__icon" viewBox="0 0 24 24" aria-hidden="true"><path d="M6 2h12v5H6zM4 8h16a2 2 0 0 1 2 2v6h-4v-3H6v3H2v-6a2 2 0 0 1 2-2zm3 6h10v8H7z"/></svg>
        415.555.0187
      </li>
      <li class="contacts__item">
        <svg class="contacts__icon" viewBox="0 0 24 24" aria-hidden="true"><path d="M2 5h20v9.5a6 6 0 0 0-8.3 5.5H2zm2 2 8 5.5L20 7v-.5H4zM18 14a4 4 0 1 1 0 8 4 4 0 0 1 0-8zm-1.8 4.2-.8.8 2 2 3-3-.8-.8-2.2 2.2z"/></svg>
        mwhitfield@brindlewood.com
      </li>
      <li class="contacts__item">
        <svg class="contacts__icon" viewBox="0 0 24 24" aria-hidden="true"><path d="M12 2a10 10 0 1 0 0 20 10 10 0 0 0 0-20zm-1 2.1V8H7.4A8 8 0 0 1 11 4.1zm2 0A8 8 0 0 1 16.6 8H13zM6.5 10H11v3H6.1a8 8 0 0 1 .4-3zm6.5 0h4.5a8 8 0 0 1 .4 3H13zm-6.6 5H11v4.9A8 8 0 0 1 6.4 15zm6.6 0h4.6a8 8 0 0 1-4.6 4.9z"/></svg>
        www.brindlewood.com
      </li>
    </ul>
  </section>

  <section class="card card--back" aria-label="Business card back">
    <div class="back-brand">
      <span class="back-brand__dot"></span>
      <p class="back-brand__name">Brindlewood First Aid</p>
    </div>
  </section>

</main>
</body>
</html>
```